Re-Design an adult education portal

I need support to re-design an adult education portal. Currently the customer has an incomplete website which should be prepared in a new format.
I have the idea how to realize, but I have no clue how to design it. The hard thing is to have a "beautiful" website with available logo and main color. I hope you can support me.

Name of Website: tovelu (tovelu.example)
Content: adult eduction for adult in safety at work, mountain climbing, dog school. various courses in different areas. But on old webpage is hard to find the different possibilities.
main color: Ral 6011 (green) -> #6C7C59
logo: you see on top of website the logo (2 dogs and a mountain with a colour gradient).

new website: for new webpage I decided to have a navigation for each section of education. In the main area I would like to have some pictures to give an idea what content is behind. At the moment it looks terrible, so I decided to use you as support for me to make the webpage prettier :). And maybe you have an better idea how to make it great. -> current state of new web page: https://tovelu.brisk-host.example/

Target Market(s)

adult eduction for adult in safety at work, mountain climbing, dog school

Number of Pages Required

1 page

Font styles to use
Serif
Sans Serif

Requirements
Must have
• As main color is set "Ral 6011" (green) -> #6C7C59

```html
<!DOCTYPE html>
<html lang="de">
<head>
<meta charset="utf-8">
<title>Tovelu – Ausbildungs- und Kurspartner</title>
<link href="https://fonts.googleapis.com/css2?family=Poppins:wght@300;400;500;600&display=swap" rel="stylesheet">
<style>
:root{
  --green:#6C7C59;
  --green-header:rgba(108,124,89,.92);
  --beige:#EEEDE3;
  --footer:#575642;
  --label:#4e5340;
  --badge:#d9dcd2;
  --white:#ffffff;
}
*{box-sizing:border-box;margin:0;padding:0}
html,body{width:1200px;height:2390px;overflow:hidden}
body{position:relative;font-family:'Poppins',sans-serif;background:var(--beige);color:var(--white)}
.abs{position:absolute}

.hero{left:0;top:0;width:1200px;height:722px;background:linear-gradient(180deg,#5f6e45 0%,#7a8a55 35%,#8a8f6a 60%,#5d6b3e 100%)}
.header{left:0;top:0;width:1200px;height:111px;background:var(--green-header)}
.brand{left:155px;top:38px;display:flex;align-items:center;gap:10px;font-size:30px;font-weight:500;color:var(--white)}
.brand-mark{width:22px;height:22px;border:2px solid var(--white)}
.contact{top:16px;display:flex;align-items:center;gap:14px}
.contact-text{font-size:14px;line-height:1.3}
.contact-text small{display:block;font-size:11px;font-weight:300}
.nav{left:436px;top:80px;width:605px;display:flex;justify-content:space-between;font-size:15px;font-weight:500}
.nav span::after{content:"";display:inline-block;width:5px;height:5px;border-right:1.5px solid #fff;border-bottom:1.5px solid #fff;transform:rotate(45deg);margin:0 0 4px 6px}

.hero-title{left:0;top:285px;width:1160px;text-align:center;font-size:51px;font-weight:500}
.hero-sub{left:150px;top:376px;width:860px;text-align:center;font-size:22px;font-weight:300;line-height:1.2}
.btn-outline{border:1.5px solid var(--white);border-radius:24px;color:var(--white);text-align:center;font-weight:500}
.hero-btn{left:489px;top:466px;width:179px;height:44px;line-height:41px;font-size:17px}

.about{left:155px;top:608px;width:886px;height:241px;background:var(--green);border-radius:6px;box-shadow:0 4px 12px rgba(0,0,0,.25)}
.about h2{position:absolute;left:41px;top:14px;font-size:29px;font-weight:500}
.about p{position:absolute;left:43px;top:68px;width:470px;font-size:13px;line-height:27px;font-weight:300}
.about-btn{left:41px;top:172px;width:116px;height:33px;line-height:30px;font-size:14px}
.badge{left:600px;top:44px;width:200px;height:130px;background:var(--badge);border-radius:10px}

.section-title{left:0;width:1200px;text-align:center;font-size:30px;font-weight:500}
.popular-title{top:886px;color:var(--green)}
.course{top:967px;width:243px;height:300px;background:var(--green);text-align:center}
.course-photo{width:100%;height:167px}
.course h3{font-size:17px;font-weight:500;margin-top:19px}
.course p{font-size:13px;font-weight:300;line-height:27px;margin-top:9px}
.arrow{top:1100px}

.band{left:0;top:1297px;width:1200px;height:771px}
.categories-title{top:1376px;color:var(--white)}
.cat{width:247px;height:247px;border-radius:50%}
.cat-label{transform:translate(-50%,-50%);background:var(--label);padding:6px 12px;font-size:17px;font-weight:500;white-space:nowrap}

.footer{left:0;top:2068px;width:1200px;height:322px;background:var(--footer)}
.footer h4{position:absolute;top:30px;font-size:16px;font-weight:500}
.footer ul{position:absolute;top:66px;list-style:none;font-size:12.5px;font-weight:300;line-height:27px}
.footer-brand{left:155px;top:196px;font-size:22px;font-weight:500;display:flex;align-items:center;gap:8px}
.copyright{left:0;top:2345px;width:1200px;text-align:center;font-size:12.5px;font-weight:300}
</style>
</head>
<body>

<div class="abs hero" role="img" aria-label="Photo of the two course leaders sitting in a green meadow with their dogs"></div>
<div class="abs header"></div>
<div class="abs brand"><span class="brand-mark"></span>tovelu.example</div>

<div class="abs contact" style="left:691px">
  <svg width="36" height="36" viewBox="0 0 36 36" fill="none" stroke="#fff" stroke-width="1.6"><path d="M9 5l5 6-3 3c2 4 5 7 9 9l3-3 6 5-3 5C14 29 6 21 5 9z"/><path d="M22 5a10 10 0 0 1 9 9M21 10a5 5 0 0 1 5 5"/></svg>
  <div class="contact-text">+41 70 555 01 23<small>Telefon</small></div>
</div>
<div class="abs contact" style="left:891px">
  <svg width="40" height="30" viewBox="0 0 40 30" fill="none" stroke="#fff" stroke-width="1.8"><rect x="2" y="2" width="36" height="26" rx="2"/><path d="M2 3l18 14L38 3M2 27l13-12M38 27L25 15"/></svg>
  <div class="contact-text">info@tovelu.example<small>E-Mail</small></div>
</div>

<nav class="abs nav">
  <span>Arbeitssicherheit</span><span>Erste Hilfe</span><span>Hundeschule</span><span>CZV</span><span>Bergausbildung</span><span>Tovelu</span>
</nav>

<h1 class="abs hero-title">Ihr Ausbildungs-und Kurspartner</h1>
<p class="abs hero-sub">Wir bieten Ihren Wünschen entsprechende Ausbildungen, zielorientiert und Ihrem Können und Wissen angepasst.</p>
<div class="abs btn-outline hero-btn">Weiterlesen</div>

<section class="abs about">
  <h2>Über Tovelu.example</h2>
  <p>Wir bieten Ihren Wünschen entsprechende Ausbildungen, zielorientiert und Ihrem Können und Wissen angepasst. Mehr zu den Kursen hier oder auf den jeweiligen Unterseiten.</p>
  <div class="abs btn-outline about-btn">Über uns</div>
  <div class="abs badge" role="img" aria-label="Partner association badge"></div>
</section>

<h2 class="abs section-title popular-title">Beliebt Ausbildungen</h2>

<svg class="abs arrow" style="left:60px" width="22" height="30" viewBox="0 0 22 30" fill="none" stroke="#6C7C59" stroke-width="3"><path d="M16 3L5 15l11 12"/></svg>
<svg class="abs arrow" style="left:1102px" width="22" height="30" viewBox="0 0 22 30" fill="none" stroke="#6C7C59" stroke-width="3"><path d="M6 3l11 12L6 27"/></svg>

<article class="abs course" style="left:155px">
  <div class="course-photo" role="img" aria-label="Yellow forklift in a warehouse aisle" style="background:linear-gradient(180deg,#6b5a48,#8a7058 60%,#3c3a36)"></div>
  <h3>Staplerkurse</h3><p>Grundausbildung</p>
</article>
<article class="abs course" style="left:476px">
  <div class="course-photo" role="img" aria-label="Trainee in a fall-protection harness on a wooden wall" style="background:linear-gradient(180deg,#9a6a3e,#7d5636 55%,#4a5c7a)"></div>
  <h3>PSAgA</h3><p>Persönliche Schutzausrüstung<br>gegen Absturz (PSAgA)</p>
</article>
<article class="abs course" style="left:798px">
  <div class="course-photo" role="img" aria-label="Orange aerial work platform in a mountain valley" style="background:linear-gradient(180deg,#8fa6c4,#7d8b86 50%,#6b6b64)"></div>
  <h3>Hubarbeitsbühne</h3><p>Bedienerschulung<br>Bedienerschulung / CZV</p>
</article>

<svg class="abs band" viewBox="0 0 1200 771" preserveAspectRatio="none"><polygon points="0,60 1200,0 1200,771 0,771" fill="#6C7C59"/></svg>
<h2 class="abs section-title categories-title">Durchsuche Kategorien</h2>

<div class="abs cat" style="left:154px;top:1460px;background:radial-gradient(circle at 45% 40%,#e8c43a,#c98a2f 55%,#6f5a3a)" role="img" aria-label="Safety helmets, ear protection and work gloves"></div>
<div class="abs cat-label" style="left:277px;top:1583px">Arbeitssicherheit</div>
<div class="abs cat" style="left:479px;top:1460px;background:radial-gradient(circle at 50% 60%,#e6dccd,#b0aeb0 55%,#7b7f8c)" role="img" aria-label="First aid training on a resuscitation dummy"></div>
<div class="abs cat-label" style="left:602px;top:1583px">Erste Hilfe</div>
<div class="abs cat" style="left:796px;top:1460px;background:radial-gradient(circle at 50% 55%,#7ab256,#4f8a3a 60%,#2f4a2a)" role="img" aria-label="Dog training on a grass field"></div>
<div class="abs cat-label" style="left:919px;top:1583px">Hundeschule</div>
<div class="abs cat" style="left:322px;top:1744px;background:radial-gradient(circle at 60% 50%,#c0484a,#9aa8bd 50%,#5a7fb8)" role="img" aria-label="Fire engine in a yard with mountains behind"></div>
<div class="abs cat-label" style="left:445px;top:1867px">CZV</div>
<div class="abs cat" style="left:638px;top:1744px;background:radial-gradient(circle at 50% 40%,#d8dde0,#8a8a84 55%,#4a4a46)" role="img" aria-label="Climbers on a rock face in the mountains"></div>
<div class="abs cat-label" style="left:761px;top:1867px">Bergausbildung</div>

<footer class="abs footer">
  <h4 style="left:155px">Tovelu GmbH</h4>
  <ul style="left:155px"><li>Lindenweg 12, CH-3900 Talbrück</li><li>Telefon: +41 70 555 01 23</li><li>E-Mail: info@tovelu.example</li></ul>
  <h4 style="left:488px">Erreichbarkeit</h4>
  <ul style="left:488px"><li>Mo-Fr: 8:00-18:00 Uhr</li><li>Sa-So: geschlossen</li></ul>
  <h4 style="left:799px">Wichtige Links</h4>
  <ul style="left:799px"><li>AGBs</li><li>Leitbild</li><li>Zertifikat Qualis</li><li>Impressum</li></ul>
  <div class="abs footer-brand" style="color:#d9d8cc">tovelu.example</div>
</footer>
<p class="abs copyright">Urheberrechte 2021 © Tovelu.example. Alle Rechte vorbehalten.</p>

</body>
</html>
```